Web Design Project for velbrook

We are looking for a sleek and sophisticated website design for our already developed web-based gallery management software application. Here is a link to our web-app: http://www.vel-brook.co

You will login on the main page and then we would like to include all of the information on the PDF that I am providing below (it outlines what?, where?, why? who? and how much?). Basically, we need a home page, about page, and a pricing page, as well as a sign up page that should be navigable from the upper right hand corner of the site where the sign in/sign up would be located. Also, our 3 tenets are that the software program is "attractive, accessible, and affordable", which might need to be somehow incorporated. There are a few websites that we would like for you to take inspiration from listed below:

https://tidemoxen.com (for homepage)
https://plumwovenly.com (for homepage/pricing page/etc)
https://tidemoxen.com/tour (for a tour of how the product works)

We are currently having a logo designed and will share that as soon as it is available! Also, let us know if you need photos/screen shots, as we can provide them.

Thanks!

Reason: Extending deadline as we are just now getting designs we would like to see fully developed.

Target Market(s)

art galleries, artists, art collectors, art consultants, museums

Industry/Entity Type

Software

Requirements
Must have
• Home page
About page (or tour through the app)
Pricing page
Sign up page (the more click-throughs to signing up the better)

```html
<!DOCTYPE html>
<html lang="en">
<head>
<meta charset="utf-8">
<title>velbrook — About</title>
<link rel="stylesheet" href="https://fonts.googleapis.com/css2?family=Arimo:wght@400;700&family=Open+Sans:ital,wght@0,400;0,600;1,400&display=swap">
<style>
:root{
  --blue:#2a83d6;
  --blue-dark:#1b64ad;
  --blue-light:#4a9ee6;
  --link:#2aa0c8;
  --ink:#222;
  --text:#444;
  --rule:#c9c9c9;
  --footer:#353535;
  --footer-text:#e6e6e6;
  --page:#ffffff;
}
*{margin:0;padding:0;box-sizing:border-box}
html,body{width:1000px;height:1200px;overflow:hidden;background:var(--page)}
body{font-family:"Arimo",Arial,sans-serif;color:var(--text);position:relative}
.site{position:absolute;left:160px;top:0;width:681px;height:1200px;background:var(--page)}
.abs{position:absolute}

/* top bar */
.topbar{left:0;top:0;width:681px;height:28px;background:var(--blue)}
.brand{left:84px;top:5px;color:#fff;font-size:14px;font-weight:700;display:flex;align-items:center;gap:5px}
.brand-dot{width:10px;height:10px;border:2px solid #fff;border-radius:50%}
.nav{right:130px;top:8px;display:flex;gap:16px;font-size:10px;color:#cfe4f7}
.nav a{color:inherit;text-decoration:none}
.nav .current{background:#1a5da3;color:#fff;padding:1px 4px;margin:-1px -4px}
.auth{right:28px;top:8px;font-size:10px;color:#fff}
.auth span{color:#9cc6ee;margin:0 4px}

/* hero */
.hero-photo{left:0;top:28px;width:681px;height:454px;
  background:linear-gradient(160deg,#b48a4a 0%,#7a6a3a 25%,#4f5a3e 45%,#6c7c88 65%,#2d3b52 85%,#8c8577 100%)}
.quote{left:402px;top:252px;width:209px;height:222px;background:rgba(40,45,55,.72);padding:30px 8px 0 26px;font-family:"Open Sans",sans-serif}
.quote-mark{position:absolute;font-size:40px;line-height:1;color:var(--blue-light);font-weight:700}
.quote-mark.open{left:12px;top:14px}
.quote-mark.close{left:162px;top:104px}
.quote p{color:#fff;font-size:12.6px;line-height:15.5px;font-weight:600;white-space:nowrap;letter-spacing:-.2px}
.quote .hl{color:var(--blue-light)}
.quote cite{display:block;margin-top:18px;font-size:9px;color:var(--blue-light);font-style:italic}
.btn{display:block;background:var(--blue);color:#fff;text-align:center;text-decoration:none;box-shadow:0 1px 2px rgba(0,0,0,.35)}
.learn{left:436px;top:417px;width:142px;height:38px;line-height:38px;font-size:17px;letter-spacing:.5px}

/* features */
.features{left:0;top:482px;width:681px;height:154px;background:linear-gradient(#f2f2f2,#e5e5e5);border-bottom:1px solid #d5d5d5}
.features h2{position:absolute;left:82px;top:14px;font-size:18px;color:var(--blue);font-weight:700}
.feature{position:absolute;top:47px;width:103px;height:72px;border-radius:4px;background:linear-gradient(var(--blue-light),var(--blue-dark));color:#fff;font-size:12px;text-align:center}
.feature::after{content:"";position:absolute;left:44px;bottom:-10px;border:8px solid transparent;border-top:6px solid var(--blue-dark);border-bottom:0;width:0}
.feature-icon{position:absolute;left:25px;top:6px;width:54px;height:42px;background:#f4f4f4;border-radius:2px}
.feature span{position:absolute;left:0;right:0;top:52px}

/* content */
.col-rule{left:383px;top:660px;height:375px;border-left:1px dotted var(--rule)}
.section-title{font-size:15px;color:var(--ink);font-weight:400;white-space:nowrap}
.title-rule{border-top:1px dotted var(--rule)}
.about-copy{left:50px;top:684px;font-size:11.3px;line-height:15.3px;color:#555;white-space:nowrap}
.devices{left:90px;top:770px}
.device-copy{left:55px;top:831px;font-size:11px;line-height:13.5px;color:#555;white-space:nowrap}
.demo{left:45px;top:875px;width:294px;height:151px;border:1px solid #bbb;box-shadow:0 2px 4px rgba(0,0,0,.25);
  background:linear-gradient(#e6e6e6 0,#e6e6e6 12px,#fff 12px)}
.demo-bar{left:62px;top:124px;width:218px;height:18px;background:#2b2b2b;border-radius:2px}
.demo-play{left:20px;top:119px;width:34px;height:22px;background:#222;border-radius:3px}

.perks{left:396px;top:698px;display:flex;gap:2px}
.perk{width:80px;text-align:center;font-size:12px;color:#333;white-space:nowrap}
.perk svg{display:block;margin:0 auto 8px}
.signup{left:460px;top:783px;width:119px;height:33px;line-height:33px;font-size:15px}

.faq{left:414px;top:885px;font-size:8.6px;line-height:13px;color:#333;white-space:nowrap}
.faq li{list-style:none;margin-bottom:5px}
.faq .answer{color:var(--link)}

/* footer */
.footer{left:0;top:1077px;width:681px;height:123px;background:var(--footer);color:var(--footer-text);font-size:8.5px}
.footer-links{position:absolute;top:34px;line-height:12.5px}
.footer-links a{display:block;color:var(--footer-text);text-decoration:none;white-space:nowrap}
.news-title,.connect-title{position:absolute;top:26px;font-size:10px}
.news-input{position:absolute;left:403px;top:43px;width:104px;height:15px;background:#fff;color:#999;font-size:10px;padding-left:3px;line-height:15px}
.news-btn{position:absolute;left:403px;top:64px;width:104px;height:15px;line-height:15px;font-size:10px}
.follow{position:absolute;left:537px;top:42px;font-size:8px;white-space:nowrap}
.follow b{color:var(--blue-light);font-weight:400}
.social{position:absolute;top:57px;width:23px;height:23px;background:#3f6a99}
.footer-brand{position:absolute;left:300px;top:76px;font-size:14px;font-weight:700;color:#fff;display:flex;align-items:center;gap:5px}
.footer-brand i{width:10px;height:10px;border:2px solid #fff;border-radius:50%}
.copy{position:absolute;left:0;right:0;top:108px;text-align:center;font-size:8px}
</style>
</head>
<body>
<div class="site">

  <header class="abs topbar">
    <div class="abs brand"><i class="brand-dot"></i>velbrook</div>
    <nav class="abs nav"><a href="#">Home</a><a href="#" class="current">About</a><a href="#">Pricing</a><a href="#">Contact</a></nav>
    <div class="abs auth">Sign in<span>|</span>Sign up</div>
  </header>

  <div class="abs hero-photo" role="img" aria-label="Photo of two young people sitting outdoors looking at a tablet together, autumn trees behind"></div>

  <blockquote class="abs quote">
    <span class="quote-mark open">&ldquo;</span>
    <p>I am <span class="hl">happy</span> lorem ipsum<br>dolor sit amet, consectetur<br>adipiscing elit. <span class="hl">velbrook</span><br>ut est pharetra, viverra velit.<br>consectetur adipiscing elit.<br>Duis ut est pharetra.</p>
    <span class="quote-mark close">&rdquo;</span>
    <cite>Maren Ostby, Freelance Designer</cite>
  </blockquote>
  <a href="#" class="abs btn learn">Learn more</a>

  <section class="abs features">
    <h2>Features</h2>
    <div class="feature" style="left:80px">
      <svg class="feature-icon" viewBox="0 0 54 42"><rect width="54" height="42" fill="#f4f4f4"/><rect x="17" y="8" width="20" height="20" fill="none" stroke="#2a83d6" stroke-width="3"/><rect x="22" y="13" width="20" height="20" fill="#2a83d6"/></svg>
      <span>galleries</span></div>
    <div class="feature" style="left:219px">
      <svg class="feature-icon" viewBox="0 0 54 42"><rect width="54" height="42" fill="#f4f4f4"/><ellipse cx="27" cy="21" rx="15" ry="11" fill="#2a83d6"/><circle cx="21" cy="17" r="2.5" fill="#f4f4f4"/><circle cx="28" cy="15" r="2.5" fill="#f4f4f4"/><circle cx="34" cy="19" r="2.5" fill="#f4f4f4"/></svg>
      <span>artists</span></div>
    <div class="feature" style="left:359px">
      <svg class="feature-icon" viewBox="0 0 54 42"><rect width="54" height="42" fill="#f4f4f4"/><circle cx="27" cy="16" r="6" fill="#2a83d6"/><path d="M17 32c0-7 20-7 20 0z" fill="#2a83d6"/></svg>
      <span>consultants</span></div>
    <div class="feature" style="left:498px">
      <svg class="feature-icon" viewBox="0 0 54 42"><rect width="54" height="42" fill="#f4f4f4"/><rect x="15" y="10" width="24" height="20" fill="none" stroke="#2a83d6" stroke-width="3"/><rect x="12" y="30" width="30" height="4" fill="#2a83d6"/></svg>
      <span>collectors</span></div>
  </section>

  <h3 class="abs section-title" style="left:49px;top:651px">What is velbrook?</h3>
  <div class="abs title-rule" style="left:49px;top:677px;width:300px"></div>
  <p class="abs about-copy">velbrook is one of the only truly web-based gallery<br>management software systems currently available for galleries,<br>artists, consultants and collectors. On a basic level, it allows you<br>to manage your artists, art inventory, clients, and invoices in one<br>clean interface that is highly integrated.</p>

  <svg class="abs devices" width="180" height="56" viewBox="0 0 180 56">
    <rect x="0" y="2" width="56" height="42" rx="3" fill="#333"/><rect x="5" y="7" width="46" height="30" fill="#fff"/>
    <rect x="22" y="44" width="12" height="6" fill="#333"/><rect x="14" y="49" width="28" height="4" rx="2" fill="#333"/>
    <rect x="64" y="0" width="16" height="52" fill="#333"/><rect x="67" y="4" width="10" height="2" fill="#fff"/><rect x="67" y="9" width="10" height="2" fill="#fff"/>
    <rect x="100" y="4" width="38" height="48" rx="4" fill="#333"/><rect x="104" y="9" width="30" height="36" fill="#fff"/>
    <rect x="155" y="12" width="24" height="40" rx="4" fill="#333"/><rect x="158" y="17" width="18" height="28" fill="#fff"/>
  </svg>
  <p class="abs device-copy">velbrook can be viewed on your mobile phone/tablet device.<br>velbrook is the easiest way to manage your art data on the cloud.</p>

  <div class="abs demo" role="img" aria-label="Screenshot of the velbrook artwork list screen with video player controls">
    <div class="abs demo-play"></div>
    <div class="abs demo-bar"></div>
  </div>

  <div class="abs col-rule"></div>

  <h3 class="abs section-title" style="left:424px;top:651px">Why choose velbrook?</h3>
  <div class="abs title-rule" style="left:405px;top:677px;width:245px"></div>
  <div class="abs perks">
    <div class="perk"><svg width="54" height="54" viewBox="0 0 54 54"><circle cx="27" cy="27" r="25.5" fill="#fff" stroke="#333" stroke-width="1.5"/><path d="M16 28a11 11 0 0 1 22 0" fill="none" stroke="#222" stroke-width="3"/><rect x="13" y="26" width="6" height="10" rx="2" fill="#222"/><rect x="35" y="26" width="6" height="10" rx="2" fill="#222"/></svg>Free Support</div>
    <div class="perk"><svg width="54" height="54" viewBox="0 0 54 54"><circle cx="27" cy="27" r="25.5" fill="#fff" stroke="#333" stroke-width="1.5"/><path d="M27 10 40 26H32V43H22V26H14z" fill="#222"/></svg>Free Upgrade</div>
    <div class="perk"><svg width="54" height="54" viewBox="0 0 54 54"><circle cx="27" cy="27" r="25.5" fill="#fff" stroke="#333" stroke-width="1.5"/><ellipse cx="27" cy="29" rx="13" ry="10" fill="none" stroke="#222" stroke-width="2"/><rect x="23" y="17" width="8" height="2" fill="#222"/><rect x="20" y="38" width="3" height="5" fill="#222"/><rect x="31" y="38" width="3" height="5" fill="#222"/></svg>Affordable</div>
  </div>
  <a href="#" class="abs btn signup">Sign up now</a>

  <h3 class="abs section-title" style="left:430px;top:844px">Frequently Asked Questions</h3>
  <div class="abs title-rule" style="left:405px;top:877px;width:245px"></div>
  <ol class="abs faq">
    <li>1. Lorem ipsum dolor sit amet, et pulvinar lacinia,<br>tellus erat interdum anteconsectetur adipiscing elit?<br><span class="answer">- Maecenas 29$ ut lacus vitae velit gravida tristique<br>vitae velit gravida.</span></li>
    <li>2. Etiam dictum pharetra turpis quis malesuada?<br><span class="answer">- Aenean sagittis lectus arcu, lacinia vulputate ipsum<br>condimentum quis.</span></li>
    <li>3. Morbi tincidunt molestie massa?<br><span class="answer">- Phasellus suscipit bibendum justo et porta.<br>Vestibulum ante ipsum primis in faucibus orci</span></li>
  </ol>

  <footer class="abs footer">
    <nav class="footer-links" style="left:46px"><a href="#">Home</a><a href="#">About us</a><a href="#">Contact us</a></nav>
    <nav class="footer-links" style="left:119px"><a href="#">FAQ</a><a href="#">Blog</a><a href="#">Sitemap</a></nav>
    <nav class="footer-links" style="left:184px"><a href="#">Community &amp; Feedback</a><a href="#">Privacy</a><a href="#">Help &amp; Support</a></nav>
    <div class="news-title" style="left:403px">Newsletter</div>
    <div class="news-input">name@mail.com</div>
    <a href="#" class="btn news-btn">Subscribe now</a>
    <div class="connect-title" style="left:558px">Connect with us</div>
    <div class="follow">Follow us on <b>Quillfeed</b> or <b>Circlebook</b></div>
    <div class="social" style="left:581px"></div>
    <div class="social" style="left:608px"></div>
    <div class="footer-brand"><i></i>velbrook</div>
    <div class="copy">© 2013 velbrook All rights reserved.</div>
  </footer>

</div>
</body>
</html>
```